Bref créative
Logo for mobile ultrasound company
Harborview Imaging Partners,LLC
Professional
Delia Warrick,RT(R)M,RDMS,RVT,RCS
Owner and Sonographer
4527 North Elmore Avenue
Fulton, MS 38916
deliaimaging@quillmail.example
www.harbimpar.example
Logo AI format
Logo EPS format

```html
<!DOCTYPE html>
<html lang="en">
<head>
<meta charset="utf-8">
<title>Harborview Imaging Partners – Stationery</title>
<link href="https://fonts.googleapis.com/css2?family=Open+Sans:wght@400;600;700&display=swap" rel="stylesheet">
<style>
  :root{
    --stage:#2e2f31;
    --paper:#ffffff;
    --ink:#2a3b55;
    --muted:#7b8494;
    --brand:#1f5fbf;
    --brand-light:#4f8fe6;
    --wave-dark:#0d0f14;
    --rule:#9aa3b0;
  }
  *{box-sizing:border-box;margin:0;padding:0}
  html,body{width:1200px;height:454px;overflow:hidden;background:var(--stage);font-family:"Open Sans",Arial,sans-serif;color:var(--ink)}
  .canvas{position:relative;width:1200px;height:454px}
  .sheet{position:absolute;background:var(--paper);overflow:hidden}
  .wave{position:absolute;left:0;bottom:0;width:100%}
  .brand{display:flex;align-items:center;gap:3px;font-weight:700;color:var(--ink);line-height:1.1}
  .brand-dot{border-radius:50%;background:var(--brand);flex:none}
  .contact{position:absolute;font-size:4px;line-height:1.35;color:var(--muted)}
  .footer-url{position:absolute;left:0;right:0;text-align:center;color:#dfe8f7;font-size:4.5px}

  /* business cards */
  .card-front{left:62px;top:150px;width:124px;height:76px}
  .card-front .brand{position:absolute;left:8px;top:12px;font-size:5px;width:70px}
  .card-front .brand-dot{width:9px;height:9px}
  .card-front .person{position:absolute;left:8px;top:32px;font-size:4.5px;line-height:1.4}
  .card-front .person b{font-size:5px;color:var(--ink)}
  .card-back{left:62px;top:250px;width:124px;height:76px}
  .card-back .brand{position:absolute;left:22px;top:26px;font-size:6px;width:90px}
  .card-back .brand-dot{width:12px;height:12px}

  /* letterhead & fax */
  .letterhead{left:206px;top:38px;width:286px;height:388px}
  .fax{left:514px;top:38px;width:286px;height:388px}
  .sheet-brand{position:absolute;left:22px;top:14px;font-size:5px;width:90px}
  .sheet-brand .brand-dot{width:11px;height:11px}
  .sheet-contact{right:30px;top:14px;width:70px}
  .fax-title{position:absolute;left:22px;top:60px;font-size:10px;font-weight:600}
  .fax-table{position:absolute;left:22px;top:78px;width:176px;border-collapse:collapse;font-size:4px;color:var(--muted)}
  .fax-table td{border:0.6px solid var(--rule);height:11px;padding:0 3px;vertical-align:middle}
  .fax-checks{position:absolute;left:22px;top:137px;width:176px;display:flex;justify-content:space-between;font-size:4px;color:var(--muted)}
  .fax-checks span::before{content:"";display:inline-block;width:4px;height:4px;border:0.6px solid var(--rule);margin-right:2px;vertical-align:middle}

  /* envelopes */
  .envelope-front{left:820px;top:100px;width:320px;height:135px}
  .envelope-front .brand{position:absolute;left:12px;top:12px;font-size:5px;width:90px}
  .envelope-front .brand-dot{width:10px;height:10px}
  .envelope-back{left:820px;top:250px;width:320px;height:135px}
  .flap{position:absolute;left:0;top:0;width:100%;height:100%}
  .envelope-back .brand{position:absolute;left:140px;top:44px;font-size:5px;width:60px}
  .envelope-back .brand-dot{width:10px;height:10px}
</style>
</head>
<body>
<main class="canvas">

  <!-- business card front -->
  <section class="sheet card-front">
    <div class="brand"><span class="brand-dot"></span>Harborview Imaging Partners,LLC</div>
    <div class="person contact" style="left:8px;top:32px;font-size:4.5px">
      <b>Delia Warrick</b><br>Owner and Sonographer<br>4527 North Elmore Avenue<br>Fulton, MS 38916<br>deliaimaging@quillmail.example
    </div>
    <svg class="wave" viewBox="0 0 124 16" height="16" preserveAspectRatio="none" aria-hidden="true">
      <path d="M0 9 C40 2 80 14 124 5 L124 16 L0 16Z" fill="var(--wave-dark)"/>
      <path d="M0 12 C40 6 80 16 124 8 L124 16 L0 16Z" fill="var(--brand)"/>
    </svg>
  </section>

  <!-- business card back -->
  <section class="sheet card-back">
    <div class="brand"><span class="brand-dot"></span>Harborview Imaging Partners,LLC</div>
  </section>

  <!-- letterhead -->
  <section class="sheet letterhead">
    <div class="brand sheet-brand"><span class="brand-dot"></span>Harborview Imaging Partners,LLC</div>
    <div class="contact sheet-contact">4527 North Elmore Avenue<br>Fulton, MS 38916<br>deliaimaging@quillmail.example<br>www.harbimpar.example</div>
    <svg class="wave" viewBox="0 0 286 60" height="60" preserveAspectRatio="none" aria-hidden="true">
      <path d="M0 30 C90 10 180 50 286 18 L286 60 L0 60Z" fill="var(--wave-dark)"/>
      <path d="M0 36 C90 18 180 56 286 26 L286 60 L0 60Z" fill="var(--brand)"/>
      <path d="M0 42 C100 30 190 60 286 40 L286 60 L0 60Z" fill="var(--brand-light)" opacity=".35"/>
    </svg>
    <div class="footer-url" style="bottom:8px">www.harbimpar.example</div>
  </section>

  <!-- fax cover -->
  <section class="sheet fax">
    <div class="brand sheet-brand"><span class="brand-dot"></span>Harborview Imaging Partners,LLC</div>
    <div class="contact sheet-contact">4527 North Elmore Avenue<br>Fulton, MS 38916<br>deliaimaging@quillmail.example<br>www.harbimpar.example</div>
    <div class="fax-title">FAX</div>
    <table class="fax-table">
      <tr><td>To:</td><td>From:</td></tr>
      <tr><td>Fax:</td><td>Pages:</td></tr>
      <tr><td>Phone:</td><td>Date:</td></tr>
      <tr><td colspan="2">Re:</td></tr>
      <tr><td colspan="2"></td></tr>
    </table>
    <div class="fax-checks"><span>Urgent</span><span>For Review</span><span>Please Reply</span><span>Recycle</span></div>
    <svg class="wave" viewBox="0 0 286 60" height="60" preserveAspectRatio="none" aria-hidden="true">
      <path d="M0 30 C90 10 180 50 286 18 L286 60 L0 60Z" fill="var(--wave-dark)"/>
      <path d="M0 36 C90 18 180 56 286 26 L286 60 L0 60Z" fill="var(--brand)"/>
      <path d="M0 42 C100 30 190 60 286 40 L286 60 L0 60Z" fill="var(--brand-light)" opacity=".35"/>
    </svg>
    <div class="footer-url" style="bottom:8px">www.harbimpar.example</div>
  </section>

  <!-- envelope front -->
  <section class="sheet envelope-front">
    <div class="brand"><span class="brand-dot"></span>Harborview Imaging Partners,LLC</div>
    <div class="contact" style="left:12px;top:28px">4527 North Elmore Avenue<br>Fulton, MS 38916</div>
    <svg class="wave" viewBox="0 0 320 40" height="40" preserveAspectRatio="none" aria-hidden="true">
      <path d="M0 22 C100 6 210 34 320 10 L320 40 L0 40Z" fill="var(--wave-dark)"/>
      <path d="M0 27 C100 12 210 40 320 17 L320 40 L0 40Z" fill="var(--brand)"/>
    </svg>
  </section>

  <!-- envelope back -->
  <section class="sheet envelope-back">
    <svg class="flap" viewBox="0 0 320 135" preserveAspectRatio="none" aria-hidden="true">
      <path d="M0 0 L160 70 L320 0" fill="none" stroke="#d4d8de" stroke-width="1"/>
      <path d="M0 135 L130 60 M320 135 L190 60" fill="none" stroke="#e3e6ea" stroke-width="1"/>
    </svg>
    <div class="brand"><span class="brand-dot"></span>Harborview Imaging</div>
  </section>

</main>
</body>
</html>
```